Tech business card design

We need an amazing business card design for our new business 'Brakka' a marketing tech startup based in Sydney, Australia. We provide an online marketplace for businesses to search and buy advertising media, connect with service providers and learn more about marketing. We wish to communicate 'cool tech', reliability and professionalism and design based around our logo.

Target Market(s)

Business Owners

Contact Information for Business Card

Name
Position
Email Address
Website
Phone Number

Font styles to use
Other font styles liked:
• Avenir & Avenir Next

Colors

Designer to choose colors to be used in the design.

```html
<!DOCTYPE html>
<html lang="en">
<head>
<meta charset="utf-8">
<title>Brakka Business Card</title>
<link rel="stylesheet" href="https://fonts.googleapis.com/css2?family=Figtree:ital,wght@0,400;0,700;0,800;0,900;1,400&display=swap">
<style>
  :root {
    --navy: #100f35;
    --ink: #3f3d56;
    --paper: #ffffff;
    --stage: #ffffff;
    --shadow: rgba(0, 0, 0, 0.28);
  }
  * { margin: 0; padding: 0; box-sizing: border-box; }
  html, body {
    width: 1200px; height: 900px; overflow: hidden;
    background: var(--stage);
    font-family: "Figtree", "Avenir Next", Arial, sans-serif;
  }
  .canvas { position: relative; width: 1200px; height: 900px; }
  .card {
    position: absolute; top: 288px;
    width: 567px; height: 324px;
    box-shadow: 0 2px 14px var(--shadow);
  }
  .card--front { left: 15px; background: var(--paper); }
  .card--back { left: 618px; background: var(--navy); }

  .contact { position: absolute; left: 28px; top: 24px; color: var(--ink); font-size: 17px; line-height: 21px; }
  .contact__name { color: var(--navy); font-size: 25px; font-weight: 700; line-height: 30px; }
  .contact__role { font-style: italic; font-size: 17px; margin-bottom: 9px; }
  .contact__label { font-weight: 700; color: var(--ink); }
  .contact__company { margin-top: 21px; font-weight: 700; }

  .front-wordmark {
    position: absolute; right: 28px; top: 22px;
    writing-mode: vertical-rl;
    color: var(--navy);
    font-size: 78px; font-weight: 900; line-height: 1;
    letter-spacing: -1px;
  }

  .back-brand { position: absolute; left: 146px; top: 100px; color: var(--paper); }
  .back-brand__name { font-size: 96px; font-weight: 900; line-height: 1; letter-spacing: -2px; }
  .back-brand__tagline { font-size: 21px; font-weight: 700; margin-top: 4px; margin-left: 2px; }
</style>
</head>
<body>
<main class="canvas">
  <section class="card card--front" aria-label="Card front">
    <div class="contact">
      <p class="contact__name">Mara Lindqvist</p>
      <p class="contact__role">Sales Manager</p>
      <p><span class="contact__label">E:</span>&nbsp; mara.l@brakka.com</p>
      <p><span class="contact__label">T:</span> (08) 5550 1294</p>
      <p><span class="contact__label">W</span>: www.brakka.com</p>
      <p class="contact__company">BRAKKA Ltd.</p>
      <p>24 Tallow Reach Lane</p>
      <p>PORT ELDRIDGE, 5402</p>
    </div>
    <p class="front-wordmark">brakka</p>
  </section>

  <section class="card card--back" aria-label="Card back">
    <div class="back-brand">
      <p class="back-brand__name">brakka</p>
      <p class="back-brand__tagline">Marketing done right!</p>
    </div>
  </section>
</main>
</body>
</html>
```